REDESIGN COUPLE PAGES FOR SURGE VIDEO ADS

PLEASE REDESIGN THIS PAGE FOR ME:
http://pagekitfinder.com/rk/milo/surge/pricing.html
I need it to be easy to read for the end user so the customer knows exactly what he will be getting. Make an emphasis on the subscription as the most popular item....and also the price per video format should be emphasized too.

Target Market(s)

B2B

Industry/Entity Type

Video Production

Number of Pages Required

3 page

Colors

Designer to choose colors to be used in the design.

Requirements
Must have
• PLEASE REDESIGN THIS PAGE FOR ME:
• http://pagekitfinder.com/rk/milo/surge/pricing.html
• I need it to be easy to read for the end user so the customer knows exactly what he will be getting. Make an emphasis on the subscription as the most popular item....and also the price per video format should be emphasized too.
Nice to have
Should not have

```html
<!DOCTYPE html>
<html lang="en">
<head>
<meta charset="utf-8">
<title>SURGE Video Ads — Pricing</title>
<link href="https://fonts.googleapis.com/css2?family=Montserrat:wght@400;500;600;700&display=swap" rel="stylesheet">
<style>
:root{
  --ink:#1d1d1f;
  --cyan:#1aa3dc;
  --blue-1:#2bb5ea;
  --blue-2:#0f6fb7;
  --purple-1:#7a2a96;
  --purple-2:#92278f;
  --orange:#f7941d;
  --red:#ec3a2a;
  --row-line:#c9c9cc;
  --panel:#f2f2f4;
  --panel-2:#fafafb;
  --tick:#6cc04a;
  --cross:#d8232a;
}
*{box-sizing:border-box;margin:0;padding:0}
html,body{width:1130px;height:1200px;overflow:hidden;background:#fff}
body{font-family:"Montserrat",sans-serif;color:var(--ink)}
.board{position:relative;width:1870px;height:1985px;transform:scale(.6043);transform-origin:0 0}
.plan{position:absolute;top:125px;width:272px;border-radius:30px;background:var(--panel-2);
  box-shadow:0 0 0 3px #d3d3d6,0 4px 8px rgba(0,0,0,.12);overflow:hidden}
.plan-head{height:140px;display:flex;flex-direction:column;align-items:center;justify-content:flex-start;padding-top:26px;
  color:#fff;text-align:center;background:linear-gradient(180deg,var(--blue-1),var(--blue-2))}
.plan-title{font-size:31px;font-weight:700;line-height:1.02;letter-spacing:-.5px;white-space:nowrap}
.plan-sub{font-size:16px;font-weight:700;margin-top:22px;line-height:1.25;letter-spacing:-.4px;white-space:nowrap}
.social .plan-head{padding-top:14px}
.social .plan-sub{margin-top:12px}
.features .plan-head{background:linear-gradient(160deg,#f7a21c,#f15a24 55%,#ef4130)}
.subscription .plan-head{background:linear-gradient(180deg,#8c3a9f,var(--purple-1))}
.price{height:145px;display:flex;flex-direction:column;align-items:center;justify-content:center;
  background:linear-gradient(180deg,#e9e9ec,var(--panel));border-bottom:5px solid var(--orange)}
.price-lead,.price-unit{font-size:21px;font-weight:700;letter-spacing:-.4px}
.price-amount{font-size:38px;font-weight:700;color:var(--cyan);margin:5px 0 4px;letter-spacing:-.5px}
.subscription .price{background:var(--purple-2);color:#fff}
.subscription .price-amount{color:#fff}
.features .price,.alacarte .price{border-bottom-color:var(--red)}
.social .price{border-bottom-color:#f9a61a}
.rows{list-style:none}
.rows li{height:52px;border-bottom:2px solid var(--row-line);display:flex;align-items:center;justify-content:center;
  font-size:14px;font-weight:500;text-transform:uppercase;letter-spacing:-.4px;white-space:nowrap;background:var(--panel-2)}
.rows li:nth-child(even){background:#fff}
.features .rows li{justify-content:flex-start;padding-left:15px;font-size:13px;letter-spacing:-.5px;background:var(--panel)}
.features .rows li:last-child{border-bottom:0}
.rows .lower{text-transform:none}
.icon{width:30px;height:30px;margin-right:8px;flex:none}
.stepper-row{height:88px;display:flex;align-items:center;justify-content:center;border-bottom:2px solid var(--row-line);background:var(--panel)}
.stepper{display:flex;background:#fff;border:1px solid #ddd;border-radius:4px}
.stepper span{width:50px;height:40px;display:flex;align-items:center;justify-content:center;font-size:24px;font-weight:500}
.stepper span+span{border-left:1px solid #ddd}
.sum{list-style:none}
.sum li{height:52px;display:flex;align-items:center;padding-left:44px;font-size:17px;letter-spacing:-.3px;white-space:nowrap;border-bottom:2px solid var(--row-line);background:var(--panel)}
.sum li span:first-child{width:132px}
.plan-foot{height:100px;display:flex;align-items:center;justify-content:center;background:linear-gradient(180deg,var(--panel),#fff)}
.buy{width:182px;height:64px;border-radius:32px;border:3px solid #0a4a86;
  background:linear-gradient(180deg,#6fd0f5,#1a8fd3 45%,#0b5ea8);color:#fff;font-size:28px;font-weight:700;
  display:flex;align-items:center;justify-content:center;letter-spacing:-.3px;box-shadow:0 3px 5px rgba(0,0,0,.25)}
</style>
</head>
<body>
<svg width="0" height="0" style="position:absolute">
  <symbol id="tick" viewBox="0 0 30 30"><circle cx="15" cy="15" r="14" fill="var(--tick)"/><path d="M8 15.5l5 5 9-10" fill="none" stroke="#fff" stroke-width="3.4" stroke-linecap="round" stroke-linejoin="round"/></symbol>
  <symbol id="cross" viewBox="0 0 30 30"><circle cx="15" cy="15" r="14" fill="var(--cross)"/><path d="M10 10l10 10M20 10l-10 10" stroke="#fff" stroke-width="3.4" stroke-linecap="round"/></symbol>
</svg>
<main class="board">

<section class="plan features" style="left:105px">
  <header class="plan-head"><h2 class="plan-title">FEATURES</h2></header>
  <div class="price"></div>
  <ul class="rows">
    <li>Videos Included</li><li>Cost per Video Format</li><li>Delivery Speed</li><li>Revisions</li><li>Final File Formats</li>
    <li>Wide Screen Video Format</li><li>Large Square Video Format</li><li>Vertical Video Format</li><li>Page Cover Video Format</li>
    <li>Holiday Theme Video</li><li>Seasonal Theme Video</li><li>Content Done for You</li><li>Full Branding in Video</li>
    <li>Full Copyright Ownership</li><li>Full Reselling Rights</li><li>Premium Video Clips</li><li>Use My Images</li>
    <li>Use My Video Footage</li><li>Use My Background Music</li><li>Fully Licensed Background Music</li>
  </ul>
</section>

<section class="plan alacarte" style="left:383px">
  <header class="plan-head"><h2 class="plan-title">AL A CARTE</h2><p class="plan-sub">AS NEEDED BASIS</p></header>
  <div class="price"><p class="price-lead">STARTS AT ONLY</p><p class="price-amount">$37.00</p><p class="price-unit">VIDEO FORMAT</p></div>
  <ul class="rows">
    <li>Custom</li><li class="lower">Starts @ $37/video</li><li>24 Hours</li><li>Unlimited</li><li class="lower">Mp4 FULL HD 1080P</li>
    <li><svg class="icon"><use href="#tick"/></svg>Included</li><li><svg class="icon"><use href="#tick"/></svg>Included</li>
    <li><svg class="icon"><use href="#tick"/></svg>Included</li><li><svg class="icon"><use href="#tick"/></svg>Included</li>
    <li>Optional</li><li>Optional</li>
    <li><svg class="icon"><use href="#tick"/></svg>Included</li><li><svg class="icon"><use href="#tick"/></svg>Included</li>
    <li><svg class="icon"><use href="#tick"/></svg>Included</li><li><svg class="icon"><use href="#tick"/></svg>Included</li>
    <li><svg class="icon"><use href="#tick"/></svg>Included</li><li><svg class="icon"><use href="#tick"/></svg>Included</li>
    <li><svg class="icon"><use href="#tick"/></svg>Included</li><li><svg class="icon"><use href="#tick"/></svg>Included</li>
    <li><svg class="icon"><use href="#tick"/></svg>Included</li>
  </ul>
  <div class="stepper-row"><div class="stepper"><span>-</span><span>1</span><span>+</span></div></div>
  <ul class="sum">
    <li><span>Total</span><span>$149</span></li><li><span>Discount</span><span>$29.80</span></li>
    <li><span>Price Per Video</span><span>$119.20</span></li><li><span>Grand Total</span><span>$119.20</span></li>
  </ul>
  <div class="plan-foot"><span class="buy">BUY NOW</span></div>
</section>

<section class="plan subscription" style="left:661px">
  <header class="plan-head"><h2 class="plan-title">SUBSCRIPTION</h2><p class="plan-sub">NEW VIDEO ADS MONTHLY</p></header>
  <div class="price"><p class="price-lead">STARTS AT ONLY</p><p class="price-amount">$16.00</p><p class="price-unit">VIDEO FORMAT</p></div>
  <ul class="rows">
    <li>Custom</li><li class="lower">Starts @ $16/video</li><li>24 Hours</li><li>Unlimited</li><li class="lower">Mp4 FULL HD 1080P</li>
    <li><svg class="icon"><use href="#tick"/></svg>Included</li><li><svg class="icon"><use href="#tick"/></svg>Included</li>
    <li><svg class="icon"><use href="#tick"/></svg>Included</li><li><svg class="icon"><use href="#tick"/></svg>Included</li>
    <li><svg class="icon"><use href="#tick"/></svg>Included</li><li><svg class="icon"><use href="#tick"/></svg>Included</li>
    <li><svg class="icon"><use href="#tick"/></svg>Included</li><li><svg class="icon"><use href="#tick"/></svg>Included</li>
    <li><svg class="icon"><use href="#tick"/></svg>Included</li><li><svg class="icon"><use href="#tick"/></svg>Included</li>
    <li><svg class="icon"><use href="#tick"/></svg>Included</li><li><svg class="icon"><use href="#tick"/></svg>Included</li>
    <li><svg class="icon"><use href="#tick"/></svg>Included</li><li><svg class="icon"><use href="#tick"/></svg>Included</li>
    <li><svg class="icon"><use href="#tick"/></svg>Included</li>
  </ul>
  <div class="stepper-row"><div class="stepper"><span>-</span><span>1</span><span>+</span></div></div>
  <ul class="sum">
    <li><span>Total</span><span>$99</span></li><li><span>Discount</span><span>$19.80</span></li>
    <li><span>Price Per Video</span><span>$79.20</span></li><li><span>Grand Total</span><span>$79.20</span></li>
  </ul>
  <div class="plan-foot"><span class="buy">BUY NOW</span></div>
</section>

<section class="plan holiday" style="left:938px">
  <header class="plan-head"><h2 class="plan-title">HOLIDAY PKG</h2><p class="plan-sub">17 HOLIDAY THEMED VIDEOS</p></header>
  <div class="price"><p class="price-lead">ONLY</p><p class="price-amount">$14.00</p><p class="price-unit">VIDEO FORMAT</p></div>
  <ul class="rows">
    <li>17</li><li class="lower">$14/video</li><li>3-5 Days</li><li>Unlimited</li><li class="lower">Mp4 FULL HD 1080P</li>
    <li><svg class="icon"><use href="#tick"/></svg>Included</li><li><svg class="icon"><use href="#tick"/></svg>Included</li>
    <li><svg class="icon"><use href="#tick"/></svg>Included</li><li><svg class="icon"><use href="#tick"/></svg>Included</li>
    <li><svg class="icon"><use href="#tick"/></svg>Included</li><li><svg class="icon"><use href="#cross"/></svg>Not Included</li>
    <li><svg class="icon"><use href="#tick"/></svg>Included</li><li><svg class="icon"><use href="#tick"/></svg>Included</li>
    <li><svg class="icon"><use href="#tick"/></svg>Included</li><li><svg class="icon"><use href="#tick"/></svg>Included</li>
    <li><svg class="icon"><use href="#tick"/></svg>Included</li><li><svg class="icon"><use href="#tick"/></svg>Included</li>
    <li><svg class="icon"><use href="#tick"/></svg>Included</li><li><svg class="icon"><use href="#tick"/></svg>Included</li>
    <li><svg class="icon"><use href="#tick"/></svg>Included</li>
  </ul>
  <div class="plan-foot"><span class="buy">BUY NOW</span></div>
</section>

<section class="plan season" style="left:1216px">
  <header class="plan-head"><h2 class="plan-title">SEASON PKG</h2><p class="plan-sub">4 SEASONAL THEMED VIDEOS</p></header>
  <div class="price"><p class="price-lead">ONLY</p><p class="price-amount">$18.00</p><p class="price-unit">VIDEO FORMAT</p></div>
  <ul class="rows">
    <li>4</li><li class="lower">$18/video</li><li>3-5 Days</li><li>Unlimited</li><li class="lower">Mp4 FULL HD 1080P</li>
    <li><svg class="icon"><use href="#tick"/></svg>Included</li><li><svg class="icon"><use href="#tick"/></svg>Included</li>
    <li><svg class="icon"><use href="#tick"/></svg>Included</li><li><svg class="icon"><use href="#tick"/></svg>Included</li>
    <li><svg class="icon"><use href="#cross"/></svg>Not Included</li><li><svg class="icon"><use href="#tick"/></svg>Included</li>
    <li><svg class="icon"><use href="#tick"/></svg>Included</li><li><svg class="icon"><use href="#tick"/></svg>Included</li>
    <li><svg class="icon"><use href="#tick"/></svg>Included</li><li><svg class="icon"><use href="#tick"/></svg>Included</li>
    <li><svg class="icon"><use href="#tick"/></svg>Included</li><li><svg class="icon"><use href="#tick"/></svg>Included</li>
    <li><svg class="icon"><use href="#tick"/></svg>Included</li><li><svg class="icon"><use href="#tick"/></svg>Included</li>
    <li><svg class="icon"><use href="#tick"/></svg>Included</li>
  </ul>
  <div class="plan-foot"><span class="buy">BUY NOW</span></div>
</section>

<section class="plan social" style="left:1493px">
  <header class="plan-head"><h2 class="plan-title">SOCIAL MEDIA<br>CALENDAR</h2><p class="plan-sub">DAILY VIDEOS FOR YOUR<br>SOCIAL MEDIA</p></header>
  <div class="price"><p class="price-lead">ONLY</p><p class="price-amount">$10.00</p><p class="price-unit">VIDEO FORMAT</p></div>
  <ul class="rows">
    <li>30</li><li class="lower">$10/video</li><li>Prior to Next Month</li><li>Unlimited</li><li class="lower">Mp4 FULL HD 1080P</li>
    <li><svg class="icon"><use href="#cross"/></svg>Not Included</li><li><svg class="icon"><use href="#tick"/></svg>Included</li>
    <li><svg class="icon"><use href="#cross"/></svg>Not Included</li><li><svg class="icon"><use href="#cross"/></svg>Not Included</li>
    <li><svg class="icon"><use href="#tick"/></svg>Included</li><li><svg class="icon"><use href="#tick"/></svg>Included</li>
    <li><svg class="icon"><use href="#tick"/></svg>Included</li><li><svg class="icon"><use href="#tick"/></svg>Included</li>
    <li><svg class="icon"><use href="#tick"/></svg>Included</li><li><svg class="icon"><use href="#tick"/></svg>Included</li>
    <li><svg class="icon"><use href="#tick"/></svg>Included</li><li><svg class="icon"><use href="#tick"/></svg>Included</li>
    <li><svg class="icon"><use href="#tick"/></svg>Included</li><li><svg class="icon"><use href="#tick"/></svg>Included</li>
    <li><svg class="icon"><use href="#tick"/></svg>Included</li>
  </ul>
  <div class="plan-foot"><span class="buy">BUY NOW</span></div>
</section>

</main>
</body>
</html>
```